Fern Gully Cleaning Tablets needs 4 x labels

We're about to launch a very exciting cleaning product to market and need your help to brand the 4 x bottles. www.ferngullyco.com.au will change the way people buy and use household cleaning products whilst significantly reducing the impact on the earth.

The tablets are dropped into the long life recycled plastic bottle, you simply add water, wait for the tab to dissolve and begin cleaning.

Target Market(s)

Women aged between 30 - 65, care for the environment, want to use less plastic, are early adopters and like to try new things. Care about a clean home and using less chemicals. Want less packaging, less plastic, less carbon emissions.

Industry/Entity Type

House Cleaning

Font styles to use
Sans Serif

Requirements
Must have
• Each label must have an obvious colour differentiator and each label must be identical in it's dimensions and information. Should look uniform when all 4 bottles are aligned in the cupboard. Limited / no images apart from logo.
Nice to have
• Simple, clear, bold, striking. Limited / no pictures. Clean lines with lots of space.
Should not have
• Sparkvane Glass Label must have a strip of blue (hex BAE1FF).
Grease Ranger Kitchen Cleaner must have a strip of colour (FFD6F3)
The Fizzer Bathroom cleaner must have a colour strip hex # FFFFBA
The Allrounder Multip Purpose must have a strip of colour Hex #BAFFC9

```html
<!DOCTYPE html>
<html lang="en">
<head>
<meta charset="utf-8">
<title>Brackenvale – Sparkvane Window Cleaner Label</title>
<link rel="stylesheet" href="https://fonts.googleapis.com/css2?family=Questrial&family=League+Gothic&family=Archivo:wght@800&display=swap">
<style>
  :root {
    --ink: #000000;
    --brand-teal: #114f5c;
    --product-blue: #00aeef;
    --label-top: #ffffff;
    --label-bottom: #bae1ff;
    --frame: #111111;
  }
  * { margin: 0; padding: 0; box-sizing: border-box; }
  html, body {
    width: 1200px;
    height: 923px;
    overflow: hidden;
    background: #ffffff;
  }
  .label {
    position: absolute;
    left: 1px;
    top: 1px;
    width: 1197px;
    height: 917px;
    overflow: hidden;
    border: 2px solid var(--frame);
    border-radius: 66px;
    background: linear-gradient(to bottom, var(--label-top) 0%, #e6f2fb 35%, var(--label-bottom) 100%);
  }
  .centered {
    position: absolute;
    left: 0;
    right: 0;
    text-align: center;
    white-space: nowrap;
  }
  .brand {
    top: 118px;
    display: flex;
    justify-content: center;
    align-items: center;
    gap: 18px;
    color: var(--brand-teal);
    font-family: "Questrial", sans-serif;
    font-size: 78px;
    line-height: 1;
  }
  .brand-dot {
    width: 34px;
    height: 34px;
    border-radius: 50%;
    background: var(--brand-teal);
  }
  .product-name {
    top: 300px;
    color: var(--product-blue);
    font-family: "Questrial", sans-serif;
    font-weight: 400;
    font-size: 132px;
    line-height: 1;
  }
  .product-type {
    top: 466px;
    color: var(--ink);
    font-family: "League Gothic", sans-serif;
    font-weight: 400;
    font-size: 162px;
    line-height: 1;
    letter-spacing: 2px;
  }
  .tagline {
    top: 672px;
    color: var(--ink);
    font-family: "Questrial", sans-serif;
    font-size: 36px;
    line-height: 1;
    word-spacing: 8px;
  }
  .volume {
    top: 744px;
    color: var(--ink);
    font-family: "Archivo", sans-serif;
    font-weight: 800;
    font-size: 44px;
    line-height: 1;
  }
  .origin {
    top: 822px;
    color: var(--ink);
    font-family: "League Gothic", sans-serif;
    font-size: 42px;
    line-height: 1;
    letter-spacing: 2px;
  }
</style>
</head>
<body>
  <main class="label">
    <div class="centered brand">
      <span class="brand-name">Brackenvale</span>
      <span class="brand-dot"></span>
    </div>
    <h1 class="centered product-name">Sparkvane</h1>
    <h2 class="centered product-type">Window Cleaner</h2>
    <p class="centered tagline">One Bottle. One Tab. Dissolve. Clean. Repeat.</p>
    <p class="centered volume">500 ml</p>
    <p class="centered origin">Wattle Bay. Australia</p>
  </main>
</body>
</html>
```